Velmora and Co Business Card Design

Looking for a business card design. Wanting Smart, Clean and Sharp looking to promote Velmora and Co, our Import Export Business - like Black, White and natural textures. I have uploaded our logo. I like a rounded font but open to other ideas
Being that we have a wide range of products on offer we are looking for a neutral yet eye catching card. We would also like to have Import - Export on the business card to be clear on want our business does.

Target Market(s)

Import export market

Industry/Entity Type

Importer

Contact Information for Business Card

Mr Tobias Kernwell
tobias.kernwell@velmoraandco.com.au
+61 (0) 417 630 284
www.velmoraandco.com.au

Font styles to use
Other font styles liked:
• Unsure of actual font name but something rounded and clean

Colors

Designer to choose colors to be used in the design.

Requirements
Must have
• Snapfold icon
• Friendlane icon

```html
<!DOCTYPE html>
<html lang="en">
<head>
<meta charset="utf-8">
<title>Velmora and Co Business Card</title>
<link rel="stylesheet" href="https://fonts.googleapis.com/css2?family=Oswald:wght@500;600&family=Open+Sans:wght@400;600&display=swap">
<style>
  :root {
    --stage: #2b2e33;
    --ink: #111111;
    --paper: #ffffff;
    --card-black: #1c1a1a;
    --silver: #c9c9c9;
    --muted: #555555;
    --rule: #1a1a1a;
  }
  * { margin: 0; padding: 0; box-sizing: border-box; }
  html, body { width: 1200px; height: 900px; overflow: hidden; }
  body {
    background: var(--stage);
    font-family: "Open Sans", Arial, sans-serif;
    position: relative;
  }
  .card {
    position: absolute;
    left: 280px;
    width: 640px;
    height: 366px;
    border-radius: 30px;
  }
  .card--back {
    top: 50px;
    background: var(--card-black);
    display: flex;
    flex-direction: column;
    align-items: center;
    justify-content: center;
    gap: 26px;
  }
  .brand {
    display: flex;
    align-items: center;
    gap: 14px;
  }
  .brand__square { width: 22px; height: 22px; flex: none; }
  .brand__name {
    font-family: "Oswald", Arial, sans-serif;
    font-weight: 600;
    text-transform: uppercase;
    letter-spacing: 1px;
    white-space: nowrap;
  }
  .card--back .brand__square { background: var(--silver); }
  .card--back .brand__name { color: var(--silver); font-size: 40px; }
  .back-url {
    color: var(--silver);
    font-size: 15px;
    letter-spacing: 4px;
  }
  .card--front {
    top: 484px;
    background: var(--paper);
    color: var(--ink);
    padding: 36px 40px;
  }
  .holder__name {
    font-family: "Oswald", Arial, sans-serif;
    font-weight: 600;
    font-size: 32px;
    line-height: 1;
    text-transform: uppercase;
    white-space: nowrap;
  }
  .holder__title {
    font-size: 13px;
    color: var(--muted);
    letter-spacing: 1px;
    margin-top: 6px;
  }
  .divider {
    position: absolute;
    left: 40px;
    right: 150px;
    top: 118px;
    height: 1.5px;
    background: var(--rule);
  }
  .card--front .brand {
    position: absolute;
    top: 40px;
    right: 40px;
  }
  .card--front .brand__square { background: var(--ink); }
  .card--front .brand__name { color: var(--ink); font-size: 26px; }
  .contacts {
    position: absolute;
    left: 40px;
    top: 140px;
    list-style: none;
    font-size: 15px;
    line-height: 28px;
  }
  .contacts li, .socials li { display: flex; align-items: center; gap: 10px; white-space: nowrap; }
  .contacts svg { width: 14px; height: 14px; fill: var(--ink); flex: none; }
  .socials {
    position: absolute;
    right: 40px;
    bottom: 34px;
    list-style: none;
    font-size: 16px;
    line-height: 30px;
    text-align: right;
  }
  .socials li { justify-content: flex-end; }
  .social-mark { width: 16px; height: 16px; background: var(--ink); border-radius: 2px; flex: none; }
</style>
</head>
<body>
  <section class="card card--back">
    <div class="brand">
      <span class="brand__square"></span>
      <span class="brand__name">Velmora and Co</span>
    </div>
    <p class="back-url">www.velmoraandco.com.au</p>
  </section>

  <section class="card card--front">
    <h1 class="holder__name">Tobias Kernwell</h1>
    <p class="holder__title">IMPORT - EXPORT</p>
    <div class="divider"></div>

    <div class="brand">
      <span class="brand__square"></span>
      <span class="brand__name">Velmora and Co</span>
    </div>

    <ul class="contacts">
      <li>
        <svg viewBox="0 0 16 16" aria-hidden="true"><rect x="1" y="3" width="14" height="10" rx="1"/><path d="M1.5 3.5 8 9l6.5-5.5" stroke="#fff" stroke-width="1.4" fill="none"/></svg>
        tobias.kernwell@velmoraandco.com.au
      </li>
      <li>
        <svg viewBox="0 0 16 16" aria-hidden="true"><path d="M4 1.5 6.3 4 5 6c.9 2 2.5 3.7 4.6 4.7l1.9-1.4 2.6 2.3-1.4 2.4C7.5 13.6 2.4 8.6 1.9 2.9z"/></svg>
        +61 (0) 417 630 284
      </li>
      <li>
        <svg viewBox="0 0 16 16" aria-hidden="true"><circle cx="8" cy="8" r="6.5"/><path d="M1.5 8h13M8 1.5c-3 3.5-3 9.5 0 13M8 1.5c3 3.5 3 9.5 0 13" stroke="#fff" stroke-width="1" fill="none"/></svg>
        www.velmoraandco.com.au
      </li>
    </ul>

    <ul class="socials">
      <li>snapfold link/ <span class="social-mark"></span></li>
      <li>friendlane link/ <span class="social-mark"></span></li>
    </ul>
  </section>
</body>
</html>
```